Design a 4-page brochure for Bramble Peak Fund

Please use the content from the Updated Brochure attachment to design a 4-page 4-color glossy letter sized brochure for Bramble Peak Fund. The content and concept of the brochure are in the attached word document. Additional photos are attached, and a logo for the fund will be forthcoming (the logo is currently a contest on ArtworkHive)
We own the attached photos that can be used in brochure.

Target Market(s)

Investors

Industry/Entity Type

Investment

```html
<!DOCTYPE html>
<html lang="en">
<head>
<meta charset="utf-8">
<title>Bramble Peak Fund – Brochure Back Cover</title>
<link href="https://fonts.googleapis.com/css2?family=Lato:wght@400;700&display=swap" rel="stylesheet">
<style>
  :root {
    --backdrop: #e9e6e1;
    --paper: #ffffff;
    --brand-blue: #1ea0d6;
    --ink: #3c3c3c;
    --photo-light: #c9c4c6;
    --photo-mid: #6d6a6c;
    --photo-dark: #1c1c1e;
  }
  * { margin: 0; padding: 0; box-sizing: border-box; }
  html, body {
    width: 1200px;
    height: 804px;
    overflow: hidden;
    background: var(--backdrop);
    font-family: "Lato", sans-serif;
  }
  .back-cover {
    position: absolute;
    left: 306px;
    top: 22px;
    width: 587px;
    height: 760px;
    background: var(--paper);
    overflow: hidden;
    box-shadow: 0 6px 18px rgba(0,0,0,0.18);
  }
  .hero-photo {
    position: absolute;
    inset: 0 0 auto 0;
    height: 470px;
    background: linear-gradient(180deg, var(--photo-light) 0%, var(--photo-mid) 28%, #3a383a 55%, var(--photo-dark) 100%);
  }
  .cover-shapes {
    position: absolute;
    inset: 0;
    width: 587px;
    height: 760px;
  }
  .disclaimer {
    position: absolute;
    left: 58px;
    top: 446px;
    width: 478px;
    font-size: 8.5px;
    line-height: 1.45;
    color: var(--ink);
    text-align: justify;
  }
  .contact {
    position: absolute;
    left: 66px;
    top: 648px;
    color: var(--paper);
    font-size: 11.5px;
    line-height: 1.5;
  }
  .contact .gap { margin-top: 10px; }
  .fund-name {
    position: absolute;
    left: 330px;
    top: 622px;
    display: flex;
    align-items: center;
    gap: 10px;
    color: var(--paper);
    font-size: 19px;
    font-weight: 400;
    letter-spacing: 0.5px;
  }
  .fund-name .mark {
    width: 34px;
    height: 34px;
    background: var(--paper);
    border-radius: 4px;
  }
</style>
</head>
<body>
  <section class="back-cover">
    <div class="hero-photo" role="img" aria-label="Photo of two businesspeople in suits shaking hands in front of a boardroom table"></div>

    <svg class="cover-shapes" viewBox="0 0 587 760" aria-hidden="true">
      <path d="M0 430 C 150 410, 300 330, 420 305 C 500 290, 560 292, 587 298 L587 760 L0 760 Z" fill="var(--paper)"/>
      <path d="M0 430 C 150 410, 300 330, 420 305 C 500 290, 560 292, 587 298" fill="none" stroke="var(--brand-blue)" stroke-width="2"/>
      <path d="M0 612 C 170 650, 380 590, 587 520 L587 760 L0 760 Z" fill="var(--brand-blue)"/>
    </svg>

    <p class="disclaimer">Investors must be “accredited investors” as defined in Regulation D of Securities Act of 1933. In addition to the financial requirements of an accredited investor, investors (either alone or with the assistance of a “purchaser representative”) must have sufficient knowledge and experience in financial and business matters generally and in securities investment in particular to allow him or her to evaluate the merits and risks of investing in the Fund. Other suitability requirements or restrictions on investment may be applicable under the laws of certain states in which the Interests may be offered. Prospective Limited Partners must also make certain representations in the Subscription Agreement relating to securities law compliance.</p>

    <address class="contact" style="font-style: normal;">
      <div>410 Larkspur Ave., Suite 210</div>
      <div>Fairhaven, USA 40210</div>
      <div class="gap">555-014-2290</div>
      <div>www.bramblepeakfund.com</div>
    </address>

    <div class="fund-name">
      <span class="mark"></span>
      <span>Bramble Peak Fund</span>
    </div>
  </section>
</body>
</html>
```